Vitoplume.com

I need a web design for a Online Wellness Center based in Chicago, IL and it's called "Vitoplume" We provide Health risk assessment to individuals and interventions. Our portal has a Health Activity tracker where our members record health activities and aerobic miles and biometric data. Our Online wellness center tracks the participant's progress toward health goals and awards points for completed activities.
I started working on this website but the designer was not able to designer a website which describes what we do. I need a fresh look on this project. I need a very attractive, responsive website which says what we do.
These are the things we do.
1. We provide Health Risk Assessments to individuals and Co-operations
2. We Provide Free health screenings to undeserved communities
3. Assist individuals access free or affordable medications
4. We ask providers/doctors to see (or do a complete physical) one individual free of charge once a year (those individuals who are no insured and don't have money to pay from their pocket)
5. Assist patient access lab work at low cost
Our goal is to provide services that will lower the cost of care for our members.

Here is the website: www.vitoplume.com still underdevelopment. PLEASE DO NOT COPY THIS STYLE OF WEBSITE. IT'S A BAD DESIGN AND THAT IS WHY I'M RE-DESIGNING THE SITE

Target Market(s)

Health individuals between the age of 21 to 65 Plus years old. Insured and uninsured

Industry/Entity Type

Health And Wellness

Coding

Coded - Design and coding required

Number of Pages Required

5+ page

Colors
0292cd

Requirements
Must have
• I'm still working on this websiteHere is the menu: Home, About us, Services, Health Screening, Providers, Contacts
• Please see. www.vitoplume.com
Nice to have
• Event calender
• Upcoming Event
• Medication
• Lab assist
• Providers/Free Clinics

```html
<!DOCTYPE html>
<html lang="en">
<head>
<meta charset="utf-8">
<title>Vitoplume — Online Wellness Center</title>
<link href="https://fonts.googleapis.com/css2?family=Open+Sans:wght@300;400;600;700&family=Raleway:wght@300;400;500;600&display=swap" rel="stylesheet">
<style>
:root{
  --brand:#0292cd;
  --brand-dark:#0278ab;
  --brand-deep:#01628c;
  --ink:#3d4246;
  --muted:#8a9096;
  --line:#e3e6e8;
  --band:#ececec;
  --white:#ffffff;
  --night:#2a2f33;
}
*{box-sizing:border-box;margin:0;padding:0}
html,body{width:1200px;height:2588px;overflow:hidden}
body{font-family:"Open Sans",Arial,sans-serif;color:var(--ink);background:var(--white);position:relative}
h1,h2,h3{font-family:"Raleway","Helvetica Neue",sans-serif;font-weight:400}
.section-title{color:var(--brand);font-size:34px;text-align:center}
.body-text{font-size:12.5px;line-height:20px;color:var(--muted)}

/* Header */
.site-header{position:absolute;top:0;left:0;width:1200px;height:110px;display:flex;align-items:center;justify-content:space-between;padding:0 80px}
.brand{display:flex;align-items:center;gap:10px;font-family:"Open Sans",sans-serif;font-weight:700;font-size:30px;color:var(--brand)}
.brand-dot{width:22px;height:22px;border-radius:50%;background:var(--brand)}
.main-nav{display:flex;gap:6px}
.main-nav a{font-size:13px;color:var(--ink);text-decoration:none;padding:10px 20px}
.main-nav a.is-active{background:var(--brand);color:var(--white)}

/* Hero */
.hero{position:absolute;top:110px;left:0;width:1200px;height:520px;background:linear-gradient(115deg,#c9b6a8 0%,#e8ddd3 35%,#d8b8a6 60%,#a58c80 100%)}
.hero-caption{position:absolute;left:80px;top:130px;width:510px;height:260px;background:rgba(255,255,255,.78);padding:30px 32px}
.hero-caption h1{color:var(--brand);font-size:30px;font-weight:500;margin-bottom:16px}
.hero-caption p{font-size:12.5px;line-height:21px;color:#555}
.slider-arrow{position:absolute;top:50%;width:34px;height:34px;margin-top:-17px}
.slider-arrow.left{left:14px}.slider-arrow.right{right:14px}

/* Welcome */
.welcome{position:absolute;top:630px;left:0;width:1200px;height:190px;padding-top:48px;text-align:center}
.welcome .body-text{width:900px;margin:26px auto 0}

/* Services */
.services{position:absolute;top:820px;left:0;width:1200px;height:340px;background:var(--band);display:flex;padding:0 80px}
.service{flex:1;text-align:center;padding:48px 22px 0;border-right:2px solid var(--white)}
.service:last-child{border-right:none}
.service-icon{width:64px;height:64px;background:var(--brand);margin:0 auto 24px;display:flex;align-items:center;justify-content:center}
.service h3{font-family:"Open Sans",sans-serif;font-size:17px;color:var(--ink);margin-bottom:14px}

/* Medication */
.medication{position:absolute;top:1160px;left:0;width:1200px;height:420px}
.medication .section-title{margin-top:46px}
.med-row{position:absolute;top:100px;left:80px;width:1040px;display:flex;gap:6px}
.med-item{flex:1;text-align:center}
.med-photo{height:140px;margin-bottom:26px}
.med-item h3{font-family:"Open Sans",sans-serif;font-size:16px;color:var(--brand);margin-bottom:12px}
.med-item .body-text{padding:0 24px}

/* Clinic banner */
.clinic{position:absolute;top:1588px;left:0;width:1200px;height:262px;background:linear-gradient(100deg,#2f3438 0%,#4a4f52 45%,#3a3e41 100%);color:var(--white);text-align:center;padding-top:92px}
.clinic h2{font-family:"Open Sans",sans-serif;font-size:27px;font-weight:400;margin-bottom:16px}
.clinic p{font-size:12.5px;line-height:22px;display:flex;justify-content:center;gap:8px;align-items:center}
.clinic .slider-arrow{top:131px}

/* Events */
.events{position:absolute;top:1850px;left:0;width:1200px;height:420px}
.events h2{position:absolute;left:80px;top:36px;color:var(--brand);font-size:32px}
.event-arrows{position:absolute;left:776px;top:50px;display:flex;gap:10px}
.event-card{position:absolute;left:80px;top:100px;width:770px;height:274px;border:1px solid var(--line);padding:12px;display:flex;gap:24px}
.event-photo{width:330px;height:248px;background:linear-gradient(135deg,#cfe3ef,#f1ede6 55%,#9fc1d6)}
.event-body{flex:1;padding-top:10px;position:relative}
.event-body h3{font-family:"Open Sans",sans-serif;font-size:17px;color:var(--brand);margin-bottom:16px}
.event-meta{position:absolute;bottom:4px;left:0;font-size:11px;color:var(--muted);display:flex;gap:22px}
.calendar{position:absolute;left:868px;top:100px;width:252px;height:274px;border:1px solid var(--line)}
.cal-head{background:var(--brand);color:var(--white);font-size:12.5px;height:38px;display:flex;align-items:center;justify-content:space-between;padding:0 12px}
.cal-grid{width:100%;border-collapse:collapse;table-layout:fixed;font-size:11px;text-align:center;color:var(--ink)}
.cal-grid th{background:#f4f5f6;font-weight:600;height:28px;border:1px solid var(--line)}
.cal-grid td{height:33px;border:1px solid var(--line)}
.cal-grid td.muted{color:#c3c7ca}
.cal-grid td.today{background:var(--brand);color:var(--white)}

/* Footer */
.site-footer{position:absolute;top:2272px;left:0;width:1200px;height:268px;background:var(--brand);color:var(--white);display:flex;padding:40px 80px 0;gap:40px}
.footer-col{flex:1}
.footer-col h4{font-family:"Raleway",sans-serif;font-size:18px;font-weight:500;margin-bottom:22px}
.footer-brand{display:flex;align-items:center;gap:8px;font-weight:700;font-size:20px;margin-bottom:20px}
.footer-brand .brand-dot{width:16px;height:16px;background:var(--white)}
.footer-list{list-style:none;font-size:11.5px;line-height:18px}
.footer-list li{display:flex;gap:10px;margin-bottom:10px;align-items:flex-start}
.bullet{width:8px;height:8px;border-radius:50%;background:var(--white);flex:none;margin-top:5px}
.field{display:block;width:100%;height:30px;background:var(--white);color:#9aa0a5;font-size:11px;padding:7px 10px;margin-bottom:10px}
.submit{display:block;width:100%;height:30px;background:var(--white);color:var(--brand);font-size:12px;font-weight:600;text-align:center;line-height:30px}
.news small{display:block;opacity:.8;font-size:10.5px}
.footer-bottom{position:absolute;top:2540px;left:0;width:1200px;height:48px;background:var(--brand-deep);color:var(--white);font-size:11px;display:flex;align-items:center;justify-content:center}
.footer-bottom span.right{position:absolute;right:80px}
</style>
</head>
<body>

<header class="site-header">
  <div class="brand"><span class="brand-dot"></span>Vitoplume</div>
  <nav class="main-nav">
    <a class="is-active" href="#">Home</a>
    <a href="#">About Us</a>
    <a href="#">Our Services</a>
    <a href="#">Health Screening</a>
    <a href="#">Providers</a>
    <a href="#">Contact Us</a>
  </nav>
</header>

<section class="hero" role="img" aria-label="Caring hands holding an elderly patient's hand">
  <div class="hero-caption">
    <h1>Vitoplume</h1>
    <p>Vitoplume is an online wellness center serving members across Chicago and beyond. We provide health risk assessments, free screenings for underserved communities and help finding affordable medication and low cost lab work. Our activity tracker records your progress toward health goals and rewards every completed activity with points you can redeem.</p>
  </div>
  <svg class="slider-arrow left" viewBox="0 0 34 34"><path d="M21 8 12 17l9 9" fill="none" stroke="#fff" stroke-width="3"/></svg>
  <svg class="slider-arrow right" viewBox="0 0 34 34"><path d="M13 8l9 9-9 9" fill="none" stroke="#fff" stroke-width="3"/></svg>
</section>

<section class="welcome">
  <h2 class="section-title">Welcome to Vitoplume</h2>
  <p class="body-text">Vitoplume brings health risk assessment, screening and medication support together in one simple online home for individuals and companies alike. Whether you are insured or uninsured, our members track daily activity, aerobic miles and biometric data, earn points for healthy habits and reach care from trusted local providers at a lower cost.</p>
</section>

<section class="services">
  <div class="service">
    <div class="service-icon"><svg width="34" height="34" viewBox="0 0 34 34"><rect x="6" y="10" width="22" height="18" rx="2" fill="none" stroke="#fff" stroke-width="2.5"/><rect x="10" y="5" width="14" height="5" fill="#fff"/><path d="M17 14v10M12 19h10" stroke="#fff" stroke-width="2.5"/></svg></div>
    <h3>Medication</h3>
    <p class="body-text">We help members find free or affordable medication through trusted programs and local pharmacy partners.</p>
  </div>
  <div class="service">
    <div class="service-icon"><svg width="34" height="34" viewBox="0 0 34 34"><rect x="4" y="6" width="26" height="18" rx="2" fill="none" stroke="#fff" stroke-width="2.5"/><path d="M8 16h5l2-5 3 9 2-4h6" fill="none" stroke="#fff" stroke-width="2"/><path d="M13 29h8" stroke="#fff" stroke-width="2.5"/></svg></div>
    <h3>Health Screening</h3>
    <p class="body-text">Free health screenings held for underserved communities, run by caring volunteer doctors and nurses.</p>
  </div>
  <div class="service">
    <div class="service-icon"><svg width="34" height="34" viewBox="0 0 34 34"><path d="M13 4h8M14 4v10L7 27a2 2 0 0 0 2 3h16a2 2 0 0 0 2-3l-7-13V4" fill="none" stroke="#fff" stroke-width="2.5"/><path d="M10 22h14" stroke="#fff" stroke-width="2"/></svg></div>
    <h3>Lab Test</h3>
    <p class="body-text">Access blood work and lab tests at low cost with our partner labs close to where you live and work.</p>
  </div>
  <div class="service">
    <div class="service-icon"><svg width="34" height="34" viewBox="0 0 34 34"><rect x="8" y="4" width="18" height="26" rx="2" fill="none" stroke="#fff" stroke-width="2.5"/><path d="M12 11h10M12 16h10M12 21h6" stroke="#fff" stroke-width="2"/></svg></div>
    <h3>Wellness Products</h3>
    <p class="body-text">Hand picked wellness products and guides that support your goals and keep your points working for you.</p>
  </div>
</section>

<section class="medication">
  <h2 class="section-title">Medication</h2>
  <div class="med-row">
    <div class="med-item">
      <div class="med-photo" role="img" aria-label="Stethoscope resting on a desk" style="background:linear-gradient(135deg,#e9eef2,#b9c8d3)"></div>
      <h3>Affordable Price</h3>
      <p class="body-text">We compare prices across programs so your medication costs stay fair and within reach.</p>
    </div>
    <div class="med-item">
      <div class="med-photo" role="img" aria-label="Medical team walking down a clinic hallway" style="background:linear-gradient(135deg,#d7dde2,#8e9aa4)"></div>
      <h3>Easy Procedure</h3>
      <p class="body-text">A short online form is all it takes to start, and our team guides you through each step.</p>
    </div>
    <div class="med-item">
      <div class="med-photo" role="img" aria-label="Doctor in a white coat in a bright office" style="background:linear-gradient(135deg,#eef3f6,#c4d6e2)"></div>
      <h3>Delivered To your Doctor</h3>
      <p class="body-text">Prescriptions are sent straight to your doctor so treatment continues without any delay.</p>
    </div>
    <div class="med-item">
      <div class="med-photo" role="img" aria-label="Pharmacist standing at pharmacy shelves" style="background:linear-gradient(135deg,#e6ecef,#a7bccb)"></div>
      <h3>Pharmacists Help</h3>
      <p class="body-text">Licensed pharmacists answer questions about dosage, refills and safe use of every medicine.</p>
    </div>
  </div>
</section>

<section class="clinic" role="img" aria-label="Dim clinic interior behind the banner text">
  <h2>Bright Path Community Clinic</h2>
  <p><svg width="10" height="14" viewBox="0 0 10 14"><path d="M5 0a5 5 0 0 0-5 5c0 4 5 9 5 9s5-5 5-9a5 5 0 0 0-5-5z" fill="#fff"/><circle cx="5" cy="5" r="2" fill="#3a3e41"/></svg>412 N. Larkspur Avenue, Carbondale, IL 62901, United States of America</p>
  <p><svg width="12" height="12" viewBox="0 0 12 12"><path d="M2 0h3l1 3-2 1a7 7 0 0 0 4 4l1-2 3 1v3a2 2 0 0 1-2 2A10 10 0 0 1 0 2a2 2 0 0 1 2-2z" fill="#fff"/></svg>(618) 555-0142</p>
  <svg class="slider-arrow left" viewBox="0 0 34 34"><path d="M21 8 12 17l9 9" fill="none" stroke="#fff" stroke-width="3"/></svg>
  <svg class="slider-arrow right" viewBox="0 0 34 34"><path d="M13 8l9 9-9 9" fill="none" stroke="#fff" stroke-width="3"/></svg>
</section>

<section class="events">
  <h2>Upcoming Event</h2>
  <div class="event-arrows">
    <svg width="14" height="14" viewBox="0 0 14 14"><path d="M9 2 4 7l5 5" fill="none" stroke="#8a9096" stroke-width="2"/></svg>
    <svg width="14" height="14" viewBox="0 0 14 14"><path d="M5 2l5 5-5 5" fill="none" stroke="#8a9096" stroke-width="2"/></svg>
  </div>
  <div class="event-card">
    <div class="event-photo" role="img" aria-label="Doctor talking with a patient holding a clipboard"></div>
    <div class="event-body">
      <h3>Health Campus</h3>
      <p class="body-text">Join our free community health day with blood pressure checks, glucose testing and one to one talks with local doctors. Members earn activity points for every screening completed, and uninsured guests can sign up for a free yearly physical with a partner provider. Families are welcome and light snacks are served.</p>
      <div class="event-meta"><span>19 Sep 2014</span><span>9:00 AM – 3:00 PM</span></div>
    </div>
  </div>
  <div class="calendar">
    <div class="cal-head">
      <svg width="10" height="10" viewBox="0 0 10 10"><path d="M7 1 3 5l4 4" fill="none" stroke="#fff" stroke-width="2"/></svg>
      <span>September - 2014</span>
      <svg width="10" height="10" viewBox="0 0 10 10"><path d="M3 1l4 4-4 4" fill="none" stroke="#fff" stroke-width="2"/></svg>
    </div>
    <table class="cal-grid">
      <tr><th>Sun</th><th>Mon</th><th>Tue</th><th>Wed</th><th>Thu</th><th>Fri</th><th>Sat</th></tr>
      <tr><td class="muted">31</td><td>1</td><td>2</td><td>3</td><td>4</td><td>5</td><td>6</td></tr>
      <tr><td>7</td><td>8</td><td>9</td><td>10</td><td>11</td><td>12</td><td>13</td></tr>
      <tr><td>14</td><td>15</td><td>16</td><td>17</td><td>18</td><td class="today">19</td><td>20</td></tr>
      <tr><td>21</td><td>22</td><td>23</td><td>24</td><td>25</td><td>26</td><td>27</td></tr>
      <tr><td>28</td><td>29</td><td>30</td><td class="muted">1</td><td class="muted">2</td><td class="muted">3</td><td class="muted">4</td></tr>
    </table>
  </div>
</section>

<footer class="site-footer">
  <div class="footer-col">
    <div class="footer-brand"><span class="brand-dot"></span>Vitoplume</div>
    <ul class="footer-list">
      <li><span class="bullet"></span>Vitoplume Inc.<br>2280 West Orchard Lane<br>Chicago IL 60614 USA</li>
      <li><span class="bullet"></span>+1 (312) 555-0187</li>
      <li><span class="bullet"></span>hello@vitoplume.com</li>
    </ul>
  </div>
  <div class="footer-col">
    <h4>Newsletter</h4>
    <span class="field">Name</span>
    <span class="field">E-mail</span>
    <span class="submit">Submit</span>
  </div>
  <div class="footer-col news">
    <h4>Recent News</h4>
    <ul class="footer-list">
      <li><span class="bullet"></span><span>Free screening day returns to the South Side<small>2 days ago</small></span></li>
      <li><span class="bullet"></span><span>New partner labs lower test costs again<small>5 days ago</small></span></li>
      <li><span class="bullet"></span><span>Tracker update adds aerobic mile goals<small>1 week ago</small></span></li>
    </ul>
  </div>
  <div class="footer-col">
    <h4>Social Media</h4>
    <ul class="footer-list">
      <li><span class="bullet"></span>Facebook</li>
      <li><span class="bullet"></span>Twitter</li>
      <li><span class="bullet"></span>Google +</li>
      <li><span class="bullet"></span>LinkedIn</li>
      <li><span class="bullet"></span>RSS</li>
    </ul>
  </div>
</footer>
<div class="footer-bottom">
  <span>© 2015 – Vitoplume.com | All Rights Reserved</span>
  <span class="right">Top</span>
</div>

</body>
</html>
```